independent cleaner, reliable, custom, thorough, trustworthy

Not sure yet if I want single-sided or double sided, so I'm selecting double-sided just in case, but single-sided designs are okay.

Really looking to find the happy medium between personal and professional in a business card design. I end up building comfortable relationships with the people I work for.

Most of my business is through referrals, but I want some business cards to hand out to people who ask for one (and maybe put them on community bulletin boards).

My target market is homeowners and business owners who are looking for a reliable cleaner and are willing to pay a bit more to have excellent quality and someone they trust.

Theme: I have a personal-professional feel since I'm solo, so the theme should reflect that. Trustworthy, personal, simple. I clean up messes.

Hopefully this is enough info, let me know if you have any questions though of course!

Target Market(s)

Homeowners businessowners who are looking for a reliable cleaner, excellent quality trustworthy.

Industry/Entity Type

Cleaning Service

Contact Information for Business Card

Please include this text:
• Delphine Warrow
• independent cleaner
• reliable, custom, thorough
• 604-317-2269
• mtb.warrow@postmail.example

Font styles to use
Serif
Sans Serif

Colors
ffffff
00a990
0492cd
33a6d7
0355a3
3276b5
919191

Requirements
Must have
• Really looking to find the happy medium between personal and professional in a business card design.
• Background: at least 50% white on the side with the most text (coloured accents or shapes are okay)
• I lean more towards simple and clean, solid colours, maybe a gentle gradient
Nice to have
• Not sure yet if I want single-sided or double sided, so I'm selecting double-sided just in case, but single-sided designs are okay.
• Colours: preferably blues and teals for the font and other objects (if any). Open to designer's choice though. I've toyed around with orangey-yellow, but it doesn't feel right and I keep going back to blues/teals
• Also I uploaded a sketch of my signature and initials so you can get a feel for my personality. I'm not expecting this to be included in the design, it's just there.
Should not have
• I don't like a lot of busy-ness or textures
• Also I don't have a logo (not sure where else to specify this)

```html
<!DOCTYPE html>
<html lang="en">
<head>
<meta charset="utf-8">
<title>Delphine Warrow – Business Card</title>
<link rel="stylesheet" href="https://fonts.googleapis.com/css2?family=Open+Sans:wght@400;600;700&display=swap">
<style>
  :root {
    --page-bg: #e9eaec;
    --card-blue: #1a5fae;
    --accent-teal: #1bb89a;
    --paper-white: #ffffff;
    --ink-blue: #1a5fae;
  }
  * { box-sizing: border-box; margin: 0; padding: 0; }
  html, body {
    width: 1200px;
    height: 976px;
    overflow: hidden;
    background: var(--page-bg);
    font-family: "Open Sans", Arial, sans-serif;
  }
  .sheet {
    position: relative;
    width: 1200px;
    height: 976px;
  }
  .card {
    position: absolute;
    left: 250px;
    width: 700px;
    height: 400px;
    box-shadow: 0 10px 28px rgba(0,0,0,0.18);
    overflow: hidden;
  }
  /* Back side */
  .card-back {
    top: 60px;
    background: var(--card-blue);
    display: flex;
    align-items: center;
    justify-content: center;
  }
  .tagline {
    display: flex;
    align-items: center;
    gap: 22px;
    color: var(--paper-white);
    font-weight: 700;
    font-size: 27px;
    letter-spacing: 1px;
    text-transform: uppercase;
  }
  .tagline-dot {
    width: 8px;
    height: 8px;
    border-radius: 50%;
    background: var(--accent-teal);
  }
  /* Front side */
  .card-front {
    top: 516px;
    background: var(--paper-white);
    display: flex;
  }
  .front-mark {
    width: 278px;
    display: flex;
    align-items: center;
    justify-content: center;
  }
  .mark-name {
    color: var(--ink-blue);
    font-weight: 600;
    font-size: 26px;
    text-align: center;
    line-height: 1.25;
  }
  .front-gap {
    width: 10px;
    background: var(--paper-white);
  }
  .teal-stripe {
    width: 12px;
    background: var(--accent-teal);
  }
  .front-gap-right {
    width: 6px;
    background: var(--paper-white);
  }
  .front-info {
    flex: 1;
    background: var(--card-blue);
    color: var(--paper-white);
    padding: 108px 0 0 108px;
  }
  .person-name {
    font-weight: 700;
    font-size: 27px;
    letter-spacing: 0.5px;
  }
  .person-role {
    font-size: 16px;
    margin-top: 2px;
  }
  .contact-list {
    list-style: none;
    margin-top: 18px;
  }
  .contact-item {
    display: flex;
    align-items: center;
    gap: 12px;
    font-size: 15px;
    margin-bottom: 6px;
  }
  .contact-icon {
    width: 14px;
    height: 14px;
    flex: none;
  }
</style>
</head>
<body>
<main class="sheet">
  <section class="card card-back" aria-label="Card back">
    <p class="tagline">
      <span>Reliable</span><span class="tagline-dot"></span>
      <span>Custom</span><span class="tagline-dot"></span>
      <span>Thorough</span>
    </p>
  </section>

  <section class="card card-front" aria-label="Card front">
    <div class="front-mark">
      <p class="mark-name">Delphine<br>Warrow</p>
    </div>
    <div class="front-gap"></div>
    <div class="teal-stripe"></div>
    <div class="front-gap-right"></div>
    <div class="front-info">
      <h1 class="person-name">Delphine Warrow</h1>
      <p class="person-role">Independent Cleaner</p>
      <ul class="contact-list">
        <li class="contact-item">
          <svg class="contact-icon" viewBox="0 0 24 24" aria-hidden="true"><path fill="#fff" d="M6.6 10.8a15.1 15.1 0 0 0 6.6 6.6l2.2-2.2a1 1 0 0 1 1-.25 11.4 11.4 0 0 0 3.6.57 1 1 0 0 1 1 1V20a1 1 0 0 1-1 1A17 17 0 0 1 3 4a1 1 0 0 1 1-1h3.5a1 1 0 0 1 1 1c0 1.25.2 2.45.57 3.6a1 1 0 0 1-.25 1z"/></svg>
          <span>604-317-2269</span>
        </li>
        <li class="contact-item">
          <svg class="contact-icon" viewBox="0 0 24 24" aria-hidden="true"><path fill="#fff" d="M2 5h20v14H2z"/><path fill="none" stroke="#1a5fae" stroke-width="2" d="M2 5l10 8 10-8"/></svg>
          <span>mtb.warrow@postmail.example</span>
        </li>
      </ul>
    </div>
  </section>
</main>
</body>
</html>
```